Cosmetic Label Design for a Sunless Tanner

We need a label for a new sunless tanner. The label dye will be 2.5 inches in height by 6 inches in width. It will be laser printed by Brevlomark.com The label will be printed on gloss laminated white polypropylene self-adhesive material. A full project description can be found in the attached Word file. The label copy is also included in a Word file.

Target Market(s)

Females aged 18 to 35

Font styles to use
Serif

Colors

Designer to choose colors to be used in the design.

Requirements
Must have
• Clean look. Strong brand image.
Nice to have
• This is the first product in a future line. The design should have the ability to move to other products.
Should not have
• Too heavy. More than 4 colors. Fonts that are whimsical. Cursive writing. No cartoon like illustrations.

```html
<!DOCTYPE html>
<html lang="en">
<head>
<meta charset="utf-8">
<title>Nourishing Sunless Tanner Label</title>
<link rel="stylesheet" href="https://fonts.googleapis.com/css2?family=Playfair+Display:wght@900&family=Cormorant+Garamond:wght@500&family=Libre+Baskerville&display=swap">
<style>
  :root {
    --backdrop: #8eadd0;
    --label-cream: #f5f4dc;
    --label-edge: #e9e8c4;
    --leaf-green: #5f7d3c;
    --leaf-light: #c9d39a;
    --rule-olive: #b3b86a;
    --ink-dark: #2e2e22;
    --outline-cream: #fbfbe8;
  }
  * { margin: 0; padding: 0; box-sizing: border-box; }
  html, body {
    width: 1200px; height: 1200px; overflow: hidden;
    background: var(--backdrop);
  }
  .canvas { position: relative; width: 1200px; height: 1200px; }
  .label {
    position: absolute; left: 50px; top: 371px;
    width: 1100px; height: 458px;
    background: linear-gradient(90deg, var(--label-edge) 0%, var(--label-cream) 12%, var(--label-cream) 88%, var(--label-edge) 100%);
    overflow: hidden;
  }
  .bamboo-art {
    position: absolute; left: 0; top: 0; width: 260px; height: 100%;
    background: linear-gradient(90deg, rgba(201,211,154,0.6) 0%, rgba(201,211,154,0.25) 60%, rgba(201,211,154,0) 100%);
  }
  .palm-art {
    position: absolute; right: 0; top: 0; width: 280px; height: 100%;
    background: radial-gradient(ellipse at 70% 30%, rgba(201,211,154,0.3) 0%, rgba(201,211,154,0) 70%);
  }
  .brand {
    position: absolute; top: 34px; left: 0; width: 100%;
    text-align: center;
    font-family: "Cormorant Garamond", serif;
    font-weight: 500;
    font-size: 36px; letter-spacing: 4px;
    color: var(--leaf-green);
  }
  .brand-rule {
    position: absolute; top: 90px; left: 380px; width: 340px; height: 2px;
    background: var(--rule-olive);
  }
  .headline {
    position: absolute; top: 104px; left: 0; width: 100%;
    text-align: center;
    font-family: "Playfair Display", serif;
    font-weight: 900;
    color: var(--leaf-green);
    line-height: 1;
    text-shadow:
      -2px -2px 0 var(--outline-cream), 2px -2px 0 var(--outline-cream),
      -2px 2px 0 var(--outline-cream), 2px 2px 0 var(--outline-cream),
      5px 4px 0 var(--leaf-light);
  }
  .headline span { display: block; }
  .headline .line-1 { font-size: 68px; letter-spacing: 2px; }
  .headline .line-2 { font-size: 78px; letter-spacing: 3px; }
  .headline .line-3 { font-size: 90px; letter-spacing: 5px; }
  .net-volume {
    position: absolute; top: 410px; left: 0; width: 100%;
    text-align: center;
    font-family: "Libre Baskerville", serif;
    font-size: 16px; color: var(--ink-dark);
  }
</style>
</head>
<body>
<div class="canvas">
  <section class="label">
    <div class="bamboo-art" role="img" aria-label="Line drawing of bamboo stalks and palm leaves along the left edge"></div>
    <div class="palm-art" role="img" aria-label="Faint palm frond drawing toward the right"></div>
    <p class="brand">SUNKISSED RITUALS</p>
    <div class="brand-rule"></div>
    <h1 class="headline">
      <span class="line-1">NOURISHING</span>
      <span class="line-2">SUNLESS</span>
      <span class="line-3">TANNER</span>
    </h1>
    <p class="net-volume">8 fl oz (237ml)</p>
  </section>
</div>
</body>
</html>
```